Banner Ad Design job - Bramblet Mortgage - Banner Ads for Re-Marketing Campaigns

Need a banner ad for a retargeting Campaign with Velvet Reach.

We would like to incorporate our attached logo. Also would like to incorporate a call to action "Pre-Qualify for a home loan today" and a button to click. This banner is to encourage previous customers to come back to our website and submit information. It must look good on mobile and desktop.

Our website is BrambletMortgage.example

Target Market(s)

Customers Seeking a Mortgage Loan

Industry/Entity Type

Mortgage Lender

Colors

Designer to choose colors to be used in the design.

Requirements
Must have
• - We would like the same basic design in the 4 sizes below.
• - 728x90 pixels leader board
• - 300x250 medium rectangle
• - 300x600 half page
• - 600x315 chatterbook
Nice to have
• Call to action. Click button or Something to promote them to click through
Should not have
• We are Open

```html
<!DOCTYPE html>
<html lang="en">
<head>
<meta charset="utf-8">
<title>Bramblet Mortgage – Pre-Qualify Banner</title>
<link rel="stylesheet" href="https://fonts.googleapis.com/css2?family=Open+Sans:wght@400;600;700&display=swap">
<style>
  :root {
    --brand-navy: #1f4f8e;
    --header-bg: #ffffff;
    --headline: #ffffff;
    --cta-bg: #f7a81b;
    --cta-text: #1e1e1e;
    --sky: #c9d3d8;
    --hillside: #8a8a78;
    --sand: #9c948a;
    --sea-deep: #3f6f84;
    --sea-light: #7ea3ad;
  }
  * { box-sizing: border-box; margin: 0; padding: 0; }
  html, body {
    width: 1200px;
    height: 630px;
    overflow: hidden;
    background: #ffffff;
  }
  .banner {
    position: relative;
    width: 1200px;
    height: 630px;
    font-family: "Open Sans", Arial, sans-serif;
    overflow: hidden;
  }
  .banner__header {
    position: absolute;
    inset: 0 0 auto 0;
    height: 140px;
    background: var(--header-bg);
  }
  .brand-name {
    position: absolute;
    left: 44px;
    top: 48px;
    color: var(--brand-navy);
    font-weight: 600;
    font-size: 34px;
    line-height: 44px;
    white-space: nowrap;
  }
  .banner__scene {
    position: absolute;
    left: 0;
    top: 140px;
    width: 1200px;
    height: 490px;
    background:
      linear-gradient(180deg, var(--sky) 0%, var(--sky) 8%, transparent 30%),
      linear-gradient(105deg, var(--hillside) 0%, var(--sand) 45%, var(--sea-light) 62%, var(--sea-deep) 100%);
  }
  .headline {
    position: absolute;
    left: 40px;
    top: 304px;
    color: var(--headline);
    font-weight: 400;
    font-size: 52px;
    line-height: 76px;
    letter-spacing: -0.3px;
    white-space: nowrap;
    text-shadow: 0 1px 4px rgba(0,0,0,0.25);
  }
  .cta {
    position: absolute;
    left: 894px;
    top: 508px;
    width: 266px;
    height: 82px;
    background: var(--cta-bg);
    color: var(--cta-text);
    font-weight: 700;
    font-size: 26px;
    letter-spacing: 0.5px;
    display: flex;
    align-items: center;
    justify-content: center;
    gap: 10px;
    text-decoration: none;
    white-space: nowrap;
  }
  .cta svg { width: 12px; height: 16px; }
</style>
</head>
<body>
  <div class="banner">
    <header class="banner__header">
      <span class="brand-name">Bramblet Mortgage</span>
    </header>

    <div class="banner__scene" role="img" aria-label="Photo of a sunny beach with waves rolling in and seaside homes along the shoreline"></div>

    <h1 class="headline">Pre–Qualify for<br>a home loan today!</h1>

    <a class="cta" href="#">CLICK HERE
      <svg viewBox="0 0 12 16" aria-hidden="true"><polygon points="0,0 12,8 0,16" fill="currentColor"/></svg>
    </a>
  </div>
</body>
</html>
```